Brackwell Immigration Law

We need a web design for our existing company www.brackwellcounselpartners.co.uk. We are an immigration consultancy. The final design should communicate professionalism, integrity and affordability.

Industry/Entity Type

It Company

Logo Text

Brackwell Counsel Partners

Number of Pages Required

5+ page

Font styles to use
Serif

Requirements
Must have
• I want to have the same silhouette logo but something different in positioning..
Nice to have
• Please have a look at these websites:
• https://www.tenderpathguide.co.uk/visa_uk/
• http://www.moorgatelegal.co.uk/
• http://www.quillfieldcounsel.org/index.php
• www.brackwellcounselpartners.co.uk

```html
<!DOCTYPE html>
<html lang="en">
<head>
<meta charset="utf-8">
<title>Brackwell Counsel Partners – Immigration Law</title>
<link href="https://fonts.googleapis.com/css2?family=Open+Sans:wght@400;600;700;800&display=swap" rel="stylesheet">
<style>
:root{
  --ink:#2b2b2b;
  --muted:#666;
  --header:#1b1b1b;
  --footer:#262626;
  --footer-deep:#161616;
  --accent:#c8102e;
  --navy:#24497a;
  --grey-bg:#ececec;
  --line:#dcdcdc;
  --white:#fff;
}
*{box-sizing:border-box;margin:0;padding:0}
html,body{width:1200px;height:2404px;overflow:hidden;background:var(--white)}
body{position:relative;font-family:"Open Sans",Arial,sans-serif;color:var(--ink);font-size:15px;line-height:1.55}
.abs{position:absolute}
/* header */
.site-header{position:absolute;left:0;top:0;width:1200px;height:112px;background:var(--header)}
.brand{position:absolute;left:24px;top:30px;display:flex;align-items:center;gap:12px;color:var(--white);font-weight:700;font-size:17px;line-height:1.15;width:220px}
.brand-mark{width:34px;height:34px;border:2px solid var(--white);flex:none}
.contact-strip{position:absolute;right:20px;top:0;display:flex;gap:10px;font-size:13px}
.contact-strip span{padding:4px 14px;color:var(--white);background:#333;border-radius:0 0 6px 6px}
.contact-strip .phone{background:var(--accent);font-weight:700}
.main-nav{position:absolute;right:20px;top:40px;display:flex}
.main-nav a{display:flex;flex-direction:column;align-items:center;width:100px;height:66px;padding-top:8px;color:var(--white);text-decoration:none;font-size:13px;gap:6px}
.main-nav a.active{background:var(--accent)}
.main-nav svg{width:22px;height:22px}
/* hero */
.hero{position:absolute;left:0;top:112px;width:1200px;height:488px;background:linear-gradient(120deg,#d9d4cc 0%,#b9b0a4 35%,#8d8274 60%,#cfc6bb 100%)}
.slide-arrow{position:absolute;top:170px;width:44px;height:44px;border-radius:50%;background:rgba(0,0,0,.45)}
.hero-caption{position:absolute;left:40px;top:392px;background:rgba(20,20,20,.75);color:var(--white);font-size:30px;font-weight:800;padding:6px 20px;letter-spacing:.3px}
/* welcome */
.welcome{position:absolute;left:50px;top:610px;width:720px}
.section-title{font-size:25px;font-weight:800;color:var(--ink);text-transform:uppercase}
.welcome p{font-size:13.5px;color:var(--muted);margin-top:10px}
.read-more{display:inline-block;margin-top:10px;font-size:13px;font-weight:700;color:var(--ink);text-decoration:none}
.visa-box{position:absolute;left:800px;top:560px;width:350px;height:210px;background:var(--white);box-shadow:0 2px 10px rgba(0,0,0,.25);padding:22px}
.visa-head{display:flex;gap:12px;align-items:center;border-bottom:1px solid var(--line);padding-bottom:14px}
.visa-icon{width:36px;height:36px;background:var(--navy)}
.visa-head h3{font-size:20px;font-weight:800;line-height:1.1}
.visa-head small{font-size:12px;color:var(--muted)}
.visa-select{margin-top:24px;height:40px;border:1px solid var(--line);display:flex;align-items:center;justify-content:space-between;padding:0 12px;font-size:13px;color:var(--muted)}
/* services */
.section-head{position:absolute;left:50px;width:1100px;display:flex;justify-content:space-between;align-items:center;border-bottom:2px solid var(--line);padding-bottom:8px}
.pager{display:flex;gap:6px}
.pager span{width:28px;height:28px;border-radius:50%;background:#555;display:flex;align-items:center;justify-content:center}
.service-card{position:absolute;top:920px;width:345px}
.service-photo{height:185px}
.service-card h4{font-size:18px;font-weight:700;margin-top:10px}
.service-card p{font-size:12.5px;color:var(--muted);line-height:1.5}
/* blog */
.blog{position:absolute;left:0;top:1250px;width:1200px;height:560px;background:var(--grey-bg)}
.post-text{position:absolute;background:var(--white);padding:26px}
.post-text h4{font-size:21px;font-weight:700;line-height:1.3}
.post-meta{font-size:12px;font-weight:700;margin-top:6px}
.post-text p{font-size:12.5px;color:var(--muted);margin-top:10px;line-height:1.5}
.post-blue{background:var(--navy);color:var(--white)}
.post-blue p,.post-blue .read-more{color:#dfe7f2}
.post-photo{position:absolute}
/* subscribe */
.subscribe{position:absolute;left:0;top:1840px;width:1200px;height:272px;background:linear-gradient(180deg,#3a3330,#201c1b);text-align:center;color:var(--white);padding-top:70px}
.subscribe h2{font-size:27px;font-weight:600}
.subscribe p{font-size:14px;color:#ccc}
.subscribe-form{display:flex;justify-content:center;gap:18px;margin-top:24px}
.field{width:320px;height:40px;background:var(--white);color:#888;font-size:13px;text-align:left;padding:10px 14px;display:flex;gap:8px;align-items:center}
.submit{width:110px;height:40px;background:var(--accent);font-weight:700;font-size:14px;padding-top:9px}
/* footer */
.site-footer{position:absolute;left:0;top:2112px;width:1200px;height:248px;background:var(--footer);color:#ddd}
.foot-col{position:absolute;top:22px}
.foot-col h5{font-size:20px;font-weight:600;color:var(--white);padding-bottom:8px;border-bottom:1px solid #555;margin-bottom:12px}
.foot-col li{list-style:none;font-size:13px;line-height:1.85}
.contact-row{display:flex;gap:10px;font-size:13px;margin-bottom:10px;line-height:1.45}
.contact-row svg{flex:none;width:16px;height:16px;margin-top:2px}
.social li{display:flex;align-items:center;gap:10px;margin-bottom:6px}
.social i{width:22px;height:22px;background:#4a4a4a;display:block}
.map{width:250px;height:150px;background:linear-gradient(135deg,#d8dccf,#b9c3b0)}
.bottom-bar{position:absolute;left:0;top:2360px;width:1200px;height:44px;background:var(--footer-deep);color:#aaa;font-size:12px;text-align:center;padding-top:13px}
</style>
</head>
<body>

<header class="site-header">
  <div class="brand"><span class="brand-mark"></span>Brackwell Counsel Partners</div>
  <div class="contact-strip">
    <span>info@brackwellcounselpartners.co.uk</span>
    <span class="phone">07700 900 418</span>
  </div>
  <nav class="main-nav">
    <a class="active" href="#"><svg viewBox="0 0 24 24" fill="none" stroke="#fff" stroke-width="2"><path d="M3 11l9-8 9 8v10H3z"/></svg>Home</a>
    <a href="#"><svg viewBox="0 0 24 24" fill="none" stroke="#fff" stroke-width="2"><rect x="3" y="7" width="18" height="13"/><path d="M9 7V4h6v3"/></svg>Work Visas</a>
    <a href="#"><svg viewBox="0 0 24 24" fill="none" stroke="#fff" stroke-width="2"><circle cx="8" cy="8" r="3"/><circle cx="16" cy="8" r="3"/><path d="M3 20c0-4 10-4 10 0M11 20c0-4 10-4 10 0"/></svg>Family Visas</a>
    <a href="#"><svg viewBox="0 0 24 24" fill="none" stroke="#fff" stroke-width="2"><rect x="4" y="3" width="16" height="18"/><path d="M8 8h8M8 12h8M8 16h5"/></svg>Business Visas</a>
    <a href="#"><svg viewBox="0 0 24 24" fill="none" stroke="#fff" stroke-width="2"><path d="M2 9l10-5 10 5-10 5z"/><path d="M6 11v5c3 3 9 3 12 0v-5"/></svg>Student Visas</a>
    <a href="#"><svg viewBox="0 0 24 24" fill="none" stroke="#fff" stroke-width="2"><circle cx="12" cy="12" r="9"/><path d="M12 11v6M12 7v1"/></svg>About us</a>
    <a href="#"><svg viewBox="0 0 24 24" fill="none" stroke="#fff" stroke-width="2"><path d="M5 12l5 5 9-10"/></svg>Get Visa</a>
    <a href="#"><svg viewBox="0 0 24 24" fill="none" stroke="#fff" stroke-width="2"><rect x="3" y="5" width="18" height="14"/><path d="M3 6l9 7 9-7"/></svg>Contact us</a>
    <a href="#"><svg viewBox="0 0 24 24" fill="none" stroke="#fff" stroke-width="2"><path d="M4 20l4-1 11-11-3-3L5 16z"/></svg>Blog</a>
  </nav>
</header>

<section class="hero" role="img" aria-label="Smiling young students outdoors, hero photograph">
  <span class="slide-arrow" style="left:8px"><svg viewBox="0 0 44 44"><path d="M25 14l-8 8 8 8" fill="none" stroke="#fff" stroke-width="3"/></svg></span>
  <span class="slide-arrow" style="right:8px"><svg viewBox="0 0 44 44"><path d="M19 14l8 8-8 8" fill="none" stroke="#fff" stroke-width="3"/></svg></span>
  <div class="hero-caption">PROVIDING ASSISTANCE REGARDING IMMIGRATION</div>
</section>

<section class="welcome">
  <h1 class="section-title">Welcome to Brackwell Counsel Partners</h1>
  <p>Lorem ipsum dolor sit amet, consectetuer adipiscing elit, sed diam nonummy nibh euismod tincidunt ut laoreet dolore magna aliquam erat volutpat. Ut wisi enim ad minim veniam, quis nostrud exerci tation ullamcorper suscipit lobortis nisl ut aliquip ex ea commodo consequat. Duis autem vel eum iriure dolor in hendrerit in vulputate velit esse molestie consequat.</p>
  <p>Vel illum dolore eu feugiat nulla facilisis at vero eros et accumsan et iusto odio dignissim qui blandit praesent luptatum zzril delenit augue duis dolore te feugait nulla facilisi.</p>
  <a class="read-more" href="#">Read More</a>
</section>

<aside class="visa-box">
  <div class="visa-head"><span class="visa-icon"></span><div><h3>VISA ASSESSMENT</h3><small>What's the best Visa for you?</small></div></div>
  <div class="visa-select">Select Visa Type<svg width="12" height="8" viewBox="0 0 12 8"><path d="M1 1l5 5 5-5" fill="none" stroke="#666" stroke-width="2"/></svg></div>
</aside>

<div class="section-head" style="top:860px">
  <h2 class="section-title">Services</h2>
  <div class="pager"><span><svg width="10" height="10" viewBox="0 0 10 10"><path d="M7 1L3 5l4 4" fill="none" stroke="#fff" stroke-width="2"/></svg></span><span><svg width="10" height="10" viewBox="0 0 10 10"><path d="M3 1l4 4-4 4" fill="none" stroke="#fff" stroke-width="2"/></svg></span></div>
</div>

<article class="service-card" style="left:50px">
  <div class="service-photo" role="img" aria-label="Business professionals group photograph" style="background:linear-gradient(135deg,#2c4f7a,#8aa7c4)"></div>
  <h4>Work Visas</h4>
  <p>Lorem ipsum dolor sit amet, consectetuer adipiscing elit, sed diam nonummy nibh euismod tincidunt. Duis autem vel eum iriure dolor in hendrerit.</p>
  <a class="read-more" href="#">Read More</a>
</article>
<article class="service-card" style="left:428px">
  <div class="service-photo" role="img" aria-label="Happy family photograph" style="background:linear-gradient(135deg,#e8d8c4,#b88e6a)"></div>
  <h4>Family Visas</h4>
  <p>Lorem ipsum dolor sit amet, consectetuer adipiscing elit, sed diam nonummy nibh euismod tincidunt. Duis autem vel eum iriure dolor in hendrerit.</p>
  <a class="read-more" href="#">Read More</a>
</article>
<article class="service-card" style="left:805px">
  <div class="service-photo" role="img" aria-label="Business meeting handshake photograph" style="background:linear-gradient(135deg,#e0e0e0,#5a5a5a)"></div>
  <h4>Business Visas</h4>
  <p>Lorem ipsum dolor sit amet, consectetuer adipiscing elit, sed diam nonummy nibh euismod tincidunt. Duis autem vel eum iriure dolor in hendrerit.</p>
  <a class="read-more" href="#">Read More</a>
</article>

<section class="blog">
  <div class="section-head" style="top:36px">
    <h2 class="section-title">Recent Blogs Posts</h2>
    <div class="pager"><span><svg width="10" height="10" viewBox="0 0 10 10"><path d="M7 1L3 5l4 4" fill="none" stroke="#fff" stroke-width="2"/></svg></span><span><svg width="10" height="10" viewBox="0 0 10 10"><path d="M3 1l4 4-4 4" fill="none" stroke="#fff" stroke-width="2"/></svg></span></div>
  </div>
  <article class="post-text" style="left:50px;top:90px;width:545px;height:220px">
    <h4>Lorem ipsum dolor sit amet, consectetuer</h4>
    <div class="post-meta">Posted: July 28, 2015 &nbsp;|&nbsp; 15 Comments</div>
    <p>Lorem ipsum dolor sit amet, consectetuer adipiscing elit, sed diam nonummy nibh euismod tincidunt ut laoreet dolore magna aliquam erat volutpat. Ut wisi enim ad minim veniam, quis nostrud exerci tation ullamcorper suscipit.</p>
    <a class="read-more" href="#">Read More</a>
  </article>
  <div class="post-photo" role="img" aria-label="Consultant meeting with clients photograph" style="left:605px;top:90px;width:545px;height:220px;background:linear-gradient(135deg,#f0ece6,#8d9aa8)"></div>
  <div class="post-photo" role="img" aria-label="Professionals in discussion photograph" style="left:50px;top:320px;width:545px;height:220px;background:linear-gradient(135deg,#c9b8a4,#6e5a4a)"></div>
  <article class="post-text post-blue" style="left:605px;top:320px;width:545px;height:220px">
    <h4>Lorem ipsum dolor sit amet, consectetuer</h4>
    <div class="post-meta">Posted: July 28, 2015 &nbsp;|&nbsp; 15 Comments</div>
    <p>Lorem ipsum dolor sit amet, consectetuer adipiscing elit, sed diam nonummy nibh euismod tincidunt ut laoreet dolore magna aliquam erat volutpat. Ut wisi enim ad minim veniam.</p>
    <a class="read-more" href="#">Read More</a>
  </article>
</section>

<section class="subscribe" role="img" aria-label="Dark city photograph behind the subscription box">
  <h2>A SUBSCRIPTION BOX</h2>
  <p>Lorem ipsum dolor sit amet, consectetur adipiscing elit. Donec non vulputate dui.</p>
  <div class="subscribe-form">
    <div class="field"><svg width="14" height="12" viewBox="0 0 14 12"><rect x="1" y="1" width="12" height="10" fill="none" stroke="#888"/><path d="M1 1l6 5 6-5" fill="none" stroke="#888"/></svg>Email Address</div>
    <div class="field"><svg width="12" height="14" viewBox="0 0 12 14"><rect x="2" y="1" width="8" height="12" rx="1" fill="none" stroke="#888"/></svg>Phone Number</div>
    <div class="submit">SUBMIT</div>
  </div>
</section>

<footer class="site-footer">
  <div class="foot-col" style="left:60px;width:180px">
    <h5>Quick Links</h5>
    <ul><li>› Home</li><li>› About Us</li><li>› Join us</li><li>› Contact us</li><li>› Blog</li><li>› Contact Us</li></ul>
  </div>
  <div class="foot-col" style="left:300px;width:280px">
    <h5>Contact Us</h5>
    <div class="contact-row"><svg viewBox="0 0 16 16"><path d="M8 15s5-5 5-9A5 5 0 003 6c0 4 5 9 5 9z" fill="#ddd"/><circle cx="8" cy="6" r="2" fill="#262626"/></svg><div><b>Brackwell Counsel Partners</b><br>118 Ashcombe Road<br>London N4 2QT</div></div>
    <div class="contact-row"><svg viewBox="0 0 16 16"><path d="M3 1h3l1 4-2 1c1 2 3 4 5 5l1-2 4 1v3c0 1-1 2-2 2C7 15 1 9 1 3c0-1 1-2 2-2z" fill="#ddd"/></svg><div>0207 946 0152</div></div>
    <div class="contact-row"><svg viewBox="0 0 16 16"><rect x="1" y="3" width="14" height="10" fill="none" stroke="#ddd" stroke-width="1.5"/><path d="M1 3l7 6 7-6" fill="none" stroke="#ddd" stroke-width="1.5"/></svg><div>enquiries@brackwellcounselpartners.co.uk</div></div>
  </div>
  <div class="foot-col" style="left:640px;width:250px">
    <h5>Location</h5>
    <div class="map" role="img" aria-label="Street map showing the office location"></div>
  </div>
  <div class="foot-col social" style="left:950px;width:200px">
    <h5>Follow Us On</h5>
    <ul><li><i></i>Friendsquare</li><li><i></i>Chirpline</li><li><i></i>Vidstream</li><li><i></i>Linkpro</li></ul>
  </div>
</footer>
<div class="bottom-bar">©Brackwell Counsel Partners 2015. All Rights Reserved.</div>

</body>
</html>
```